Exciting new aperitif brand needs a great label

Vel-Orin is a wonderful rich new premium-priced bitter aperitif, with a deep red colour, from a 100+ year old distillery (1890) near Turin in the Piedmont region of Italy. Inspired by Torvesi, it is perfectly formulated to elevate the classic Baldetti cocktail (and variations on it). It also goes perfectly in a Spritz or a long mixed drink with soda or tonic. The name Vel-Orin is derived from the French for 'peak' and the Italian word for 'love'.

The label, which should take inspiration from Torvesi, but be distinctively different, can incoporate any number of premium label embellishments (foil, embossing, textures etc) and should be no greater than 11cm (height) x 9cm (width) with any core imagery restricted to a width of c.7cm.

The attached mood board should act as inspiration and colour should largely be restricted to reds, blues, whites and perhaps orange. For completeness, the label should note that the ABV is 25% and the bottle size 70cl.

Target Market(s)

21-45yr olds - equal split female/male

Colors
0054AA
0677BA
7BADD7
CADEEF
E8F1F8
0094D4
00A9DD
6FCCEA
C7EBF8
E9F6FB
EE7325
F08F49
F5BC92
FAE3D3
FDF4ED
EB3D1F
EC4F4E
F09395
F8D3D4
FCEDEE

Requirements
Must have
• Great lettering design on the name Vel-Orin

```html
<!DOCTYPE html>
<html lang="en">
<head>
<meta charset="utf-8">
<title>Vel-Orin Bitter – Label</title>
<link rel="stylesheet" href="https://fonts.googleapis.com/css2?family=Alfa+Slab+One&family=Great+Vibes&family=Playfair+Display:wght@400&family=Montserrat:wght@300;700&display=swap">
<style>
  :root {
    --paper: #ffffff;
    --navy: #0e1b3c;
    --gold-light: #fff3a6;
    --gold-mid: #e9b62a;
    --gold-deep: #9a5a12;
    --gold-text: #d9a33a;
    --name-white: #eeeeee;
    --mist: #a9b7bf;
    --stone: #8f979c;
    --rock: #7b8489;
    --soft-white: #dfe3ea;
  }
  html, body {
    margin: 0;
    padding: 0;
    width: 1200px;
    height: 1200px;
    overflow: hidden;
    background: var(--paper);
  }
  .label-canvas { display: block; width: 1200px; height: 1200px; }
  .stop-gold-light { stop-color: var(--gold-light); }
  .stop-gold-mid { stop-color: var(--gold-mid); }
  .stop-gold-deep { stop-color: var(--gold-deep); }
  .stop-mist { stop-color: var(--mist); }
  .stop-stone { stop-color: var(--stone); }
  .stop-rock { stop-color: var(--rock); }
  .navy { fill: var(--navy); }
  .gold { fill: url(#goldSheen); }
  .gold-fold { fill: var(--gold-deep); }
  .brand-name {
    font-family: "Alfa Slab One", "Rockwell", serif;
    font-size: 140px;
    fill: var(--name-white);
  }
  .since, .region { font-family: "Great Vibes", cursive; }
  .since { font-size: 40px; fill: var(--gold-text); }
  .region { font-size: 46px; fill: var(--soft-white); }
  .year {
    font-family: "Playfair Display", serif;
    font-size: 72px;
    fill: var(--gold-text);
  }
  .spec {
    font-family: "Montserrat", sans-serif;
    font-weight: 300;
    font-size: 25px;
    fill: var(--soft-white);
  }
  .spec-type {
    font-family: "Montserrat", sans-serif;
    font-weight: 700;
    font-size: 28px;
    letter-spacing: 1px;
    fill: var(--gold-text);
  }
</style>
</head>
<body>
<svg class="label-canvas" viewBox="0 0 1200 1200" xmlns="http://www.w3.org/2000/svg">
  <defs>
    <linearGradient id="goldSheen" x1="0" y1="0" x2="1" y2="1">
      <stop offset="0" class="stop-gold-deep"/>
      <stop offset="0.3" class="stop-gold-mid"/>
      <stop offset="0.5" class="stop-gold-light"/>
      <stop offset="0.7" class="stop-gold-mid"/>
      <stop offset="1" class="stop-gold-deep"/>
    </linearGradient>
    <linearGradient id="mountainTones" x1="0" y1="0" x2="0" y2="1">
      <stop offset="0" class="stop-mist"/>
      <stop offset="0.5" class="stop-stone"/>
      <stop offset="1" class="stop-rock"/>
    </linearGradient>
  </defs>

  <g class="label" transform="translate(117,-128)">
    <!-- outer frame with peaked top edge -->
    <path class="label-frame gold" d="M130 330 H270 L298 298 L330 330 H525 L580 272 L650 330 H835 V1185 H130 Z"/>
    <path class="label-field navy" d="M148 348 H278 L298 322 L318 348 H532 L580 296 L632 348 H817 V1165 H148 Z"/>

    <!-- illustration area -->
    <path class="mountain-scene" role="img" aria-label="Illustration of snow-capped alpine mountain peaks under a navy sky"
          fill="url(#mountainTones)"
          d="M148 348 H278 L298 322 L318 348 H532 L580 296 L632 348 H817 V665 H148 Z"/>

    <!-- ribbon folds -->
    <polygon class="gold-fold" points="70,905 130,905 130,945"/>
    <polygon class="gold-fold" points="895,905 835,905 835,945"/>

    <!-- name banner with heart crest and chevron point -->
    <path class="name-banner gold"
          d="M70 665 H290 C290 600 380 570 482 650 C584 570 674 600 674 665 H895 V905 H560 L482 968 L404 905 H70 Z"/>
    <path class="name-banner-field navy"
          d="M90 685 H305 C310 625 385 600 482 672 C579 600 654 625 659 685 H875 V885 H552 L482 940 L412 885 H90 Z"/>

    <text class="brand-name" x="490" y="838" text-anchor="middle" textLength="710" lengthAdjust="spacingAndGlyphs">VEL-ORIN</text>

    <!-- heritage mark -->
    <text class="since" x="490" y="993" text-anchor="middle">since</text>
    <text class="year" x="486" y="1055" text-anchor="middle">1890</text>
    <text class="region" x="492" y="1082" text-anchor="middle">Piedmont</text>

    <!-- specs -->
    <text class="spec" x="258" y="1140" text-anchor="middle">25% ABV</text>
    <text class="spec-type" x="486" y="1142" text-anchor="middle">BITTER</text>
    <text class="spec" x="703" y="1140" text-anchor="middle">700ML</text>
  </g>
</svg>
</body>
</html>
```